Flyer Design Project

I need to create a flyer to advertise an Luxury Self Catering Apartment Complex in a Ski Resort in Europe. The development offers luxury accommodation to those who are on a budget.

Below is what needs to be included and a basic layout design idea i had that can be changed. The information is important. Hoping to get it on a flyer sized 21.6 x 14 cm

Title - 'Luxury Self Catering Ski Apartments For Rent'
Sub Title - 'Located 200m from Gondola, Restaurants and Bars'

Studio - Sleeps 1-2 - From only £200 per week
1 Bed - Sleeps 2-4 - From only £250 per week
2 Bed - Sleeps 4-6 - From only £350 per week

Image 1 Image 2 Image 3

- Fully Furnished Modern, Spacious & Comfortable Apartments
- Fully Staffed Development (Reception, Bar + Daily Cleaning)
- Family friendly & suitable for children of all ages

(Twitter Icon) @snowlarkchalets
E-mail - snowlarkchalets@mailvora.co.uk
Telephone - +44 (0) 7811 302 684

Target Market(s)

Our target market is very wide. We are trying to attract students, couples and families who are skiing on a budget.

Industry/Entity Type

Accommodation

Requirements
Must have
• The text contained in 'task description' is important but i'd like to be led on design. Size of around 21.6 x 14cm is important and i'd like the 3 images below (hopefully someone can get of the date and time in orange bottom right of all pics)

http://i2217.picvaultra.com/albums/kq412/tmwimages/Bansko/699_00_640_zpsd7b2ba81.jpeg

http://i2217.picvaultra.com/albums/kq412/tmwimages/Bansko/a_02_zps7503dd10.jpeg

http://i2217.picvaultra.com/albums/kq412/tmwimages/Bansko/699_08_640_zps2f11bf21.jpeg

```html
<!DOCTYPE html>
<html lang="en">
<head>
<meta charset="utf-8">
<title>Luxury Self Catering Ski Apartments Flyer</title>
<link href="https://fonts.googleapis.com/css2?family=Source+Sans+3:wght@400;600;700&display=swap" rel="stylesheet">
<style>
  :root {
    --page-bg: #e9e4dc;
    --flyer-dark: #141312;
    --flyer-mid: #3a3836;
    --band-brown: #2e231c;
    --text-light: #ffffff;
    --text-soft: #e4e4e4;
    --icon-blue: #3aa0db;
    --photo-building: #7d776f;
    --photo-lounge: #6b4a33;
    --photo-bedroom: #9a8461;
  }
  html, body {
    margin: 0;
    width: 1200px;
    height: 1000px;
    overflow: hidden;
    background: var(--page-bg);
    font-family: "Source Sans 3", "Myriad Pro", Arial, sans-serif;
  }
  .flyer {
    position: absolute;
    left: 50px;
    top: 143px;
    width: 1100px;
    height: 713px;
    overflow: hidden;
    color: var(--text-light);
    background:
      radial-gradient(ellipse 60% 45% at 78% 8%, rgba(200,205,210,.55), transparent 70%),
      radial-gradient(ellipse 50% 40% at 15% 20%, rgba(120,118,115,.45), transparent 70%),
      linear-gradient(180deg, #4b4a4a 0%, #2a2928 38%, var(--flyer-dark) 60%, #1c1816 100%);
    box-shadow: 0 6px 18px rgba(0,0,0,.35);
  }
  .header-band {
    position: absolute;
    left: 0; top: 0;
    width: 100%; height: 273px;
    background: linear-gradient(90deg, rgba(255,255,255,.04), rgba(255,255,255,.1) 70%, rgba(255,255,255,.18));
  }
  .title {
    position: absolute;
    top: 52px; left: 0; width: 100%;
    margin: 0;
    text-align: center;
    font-weight: 600;
    font-size: 44px;
    letter-spacing: .2px;
  }
  .subtitle {
    position: absolute;
    top: 110px; left: 0; width: 100%;
    margin: 0;
    text-align: center;
    font-weight: 400;
    font-size: 24px;
    color: var(--text-soft);
  }
  .prices {
    position: absolute;
    top: 163px; left: 0; width: 100%;
    margin: 0; padding: 0;
    list-style: none;
    text-align: center;
    font-weight: 700;
    font-size: 21px;
    line-height: 36px;
  }
  .gallery .photo {
    position: absolute;
    top: 303px;
    width: 292px;
    height: 219px;
  }
  .photo-building { left: 63px; background: linear-gradient(180deg, #b9c7d6 0%, var(--photo-building) 45%, #4d4640 100%); }
  .photo-lounge { left: 404px; background: linear-gradient(90deg, var(--photo-lounge) 0%, #d9d1c2 45%, #8a6240 75%, #3a2619 100%); }
  .photo-bedroom { left: 743px; background: linear-gradient(180deg, #c8b68f 0%, var(--photo-bedroom) 50%, #e8e4dc 80%, #5a4330 100%); }
  .info-band {
    position: absolute;
    left: 0; top: 551px;
    width: 100%; height: 162px;
    background: linear-gradient(90deg, #3a2b21 0%, var(--band-brown) 50%, #1f1915 100%);
  }
  .features {
    position: absolute;
    left: 68px; top: 569px;
    margin: 0; padding: 0;
    list-style: none;
    font-size: 21px;
    line-height: 35.5px;
    color: var(--text-soft);
  }
  .contacts {
    position: absolute;
    left: 720px; top: 569px;
    margin: 0; padding: 0;
    list-style: none;
    font-size: 21px;
    line-height: 35.5px;
    color: var(--text-soft);
  }
  .contacts li { display: flex; align-items: center; gap: 9px; }
  .contacts .icon { width: 26px; height: 26px; flex: none; }
  .handle-mark { width: 24px; height: 24px; background: var(--icon-blue); border-radius: 3px; flex: none; margin-right: 2px; }
</style>
</head>
<body>
  <article class="flyer">
    <div class="header-band"></div>
    <h1 class="title">Luxury Self Catering Ski Apartments For Rent</h1>
    <p class="subtitle">Located 200m from Gondola, Restaurants and Bars</p>
    <ul class="prices">
      <li>Studio - Sleeps 1-2 - From only £200 per week</li>
      <li>1 Bed - Sleeps 2-4 - From only £250 per week</li>
      <li>2 Bed - Sleeps 4-6 - From only £350 per week</li>
    </ul>

    <div class="gallery">
      <div class="photo photo-building" role="img" aria-label="Exterior of the stone-clad apartment building under a blue sky"></div>
      <div class="photo photo-lounge" role="img" aria-label="Apartment living room with sofa, armchair and curtained window"></div>
      <div class="photo photo-bedroom" role="img" aria-label="Apartment bedroom with white double bed and desk"></div>
    </div>

    <div class="info-band"></div>
    <ul class="features">
      <li>Fully Furnished Modern, Spacious &amp; Comfortable Apartments</li>
      <li>Fully Staffed Development (Reception, Bar + Daily Cleaning)</li>
      <li>Family friendly &amp; suitable for children of all ages</li>
    </ul>
    <ul class="contacts">
      <li><span class="handle-mark"></span>@snowlarkchalets</li>
      <li>
        <svg class="icon" viewBox="0 0 26 26" aria-hidden="true">
          <rect x="2" y="6" width="22" height="15" rx="1" fill="var(--icon-blue)"/>
          <path d="M2 7 L13 15 L24 7" fill="none" stroke="#1b1b1b" stroke-width="1.6"/>
        </svg>
        snowlarkchalets@mailvora.co.uk
      </li>
      <li>
        <svg class="icon" viewBox="0 0 26 26" aria-hidden="true">
          <path d="M7 3 L10 3 L12 9 L9.5 11 Q12 16 16 18.5 L18 16 L24 18 L24 21 Q23 24 19 23.5 Q9 21 3.5 9 Q3 4 7 3 Z" fill="var(--icon-blue)"/>
        </svg>
        +44 (0) 7811 302 684
      </li>
    </ul>
  </article>
</body>
</html>
```